The Harvest Ledger App - Modernization & Graphics User Interface Friendliness Updates

We are Harvest Ledger, and we want to bring a new branding look and graphical user interface to the Harvest Ledger App. The app is a quick reference encyclopedia for all things produce. Boasting articles on over 2,000 produce items, with information ranging from taste and application to geographical and cultural significance. Included in its features are over 10 thousand recipes, and the Harvest Ledger App Crop Bazaar – a global initiative to connect farmer, customer, and chef in one sustainable and easy to use application. The design needs to bring a greater sense of social connection – encouraging the user to participate in the 'Crop Bazaar' experience voluntarily. The design should reflect a sense of authority reflecting the authenticity and reliability of the provided information, it's writing, and its sources. Download the App here: hvldg.example/get

Target Market(s)

Women and Men between ages 21-55.

Industry/Entity Type

Education

Font styles to use
Serif
Sans Serif

Colors

Designer to choose colors to be used in the design.

Requirements
Must have
• An updated user interface, the intuitive usability of the app is currently non-existent. We are looking to reflect as the authority on produce. The app design must reflect a professional, user-friendly, up-to-date, and trustworthy feel.
Nice to have
• To incorporate the social draw of the Crop Bazaar we would like to include on the home page "Social Bubbles" (think Pictaloo stories) which updates with shared photos of produce and their location.
Should not have
• An overly complicated theme, distracting or unprofessional colors, and images.

```html
<!DOCTYPE html>
<html lang="en">
<head>
<meta charset="utf-8">
<title>Harvest Ledger – Produce Detail</title>
<link href="https://fonts.googleapis.com/css2?family=Raleway:wght@300&family=Source+Sans+3:wght@400&display=swap" rel="stylesheet">
<style>
  :root {
    --page-bg: #f2f2f3;
    --screen-bg: #ffffff;
    --photo-top: #565a63;
    --photo-mid: #a9abb0;
    --photo-bottom: #e9e9eb;
    --status-text: #ffffff;
    --title-ink: #2d3340;
    --meta-ink: #a3a9b1;
    --body-ink: #555a62;
    --heading-ink: #2b2f36;
    --rating-ink: #4a4e55;
    --accent-red: #ef4d5e;
    --divider: #e6e7ea;
  }
  * { margin: 0; padding: 0; box-sizing: border-box; }
  html, body { width: 1200px; height: 1200px; overflow: hidden; }
  body {
    background: var(--page-bg);
    font-family: "Source Sans 3", "Source Sans Pro", sans-serif;
    position: relative;
  }
  .screen {
    position: absolute;
    left: 275px; top: 20px;
    width: 650px; height: 1160px;
    background: var(--screen-bg);
    overflow: hidden;
  }
  .hero-photo {
    position: absolute; left: 0; top: 0;
    width: 650px; height: 668px;
    background: linear-gradient(180deg, var(--photo-top) 0%, var(--photo-mid) 42%, var(--photo-bottom) 78%, var(--photo-bottom) 100%);
  }
  .status-bar {
    position: absolute; left: 0; top: 0; width: 650px; height: 42px;
    color: var(--status-text);
    font-size: 21px;
    display: flex; align-items: center; justify-content: space-between;
    padding: 0 12px 0 14px;
  }
  .status-left, .status-right { display: flex; align-items: center; gap: 6px; width: 200px; }
  .status-right { justify-content: flex-end; }
  .signal { display: flex; gap: 3px; }
  .signal span { width: 10px; height: 10px; border-radius: 50%; border: 1.5px solid var(--status-text); }
  .signal span.on { background: var(--status-text); }
  .battery { width: 40px; height: 17px; border: 1.5px solid var(--status-text); border-radius: 4px; position: relative; padding: 2px; }
  .battery::after { content: ""; position: absolute; right: -5px; top: 5px; width: 3px; height: 6px; background: var(--status-text); border-radius: 0 2px 2px 0; }
  .battery-level { width: 40%; height: 100%; background: var(--status-text); border-radius: 1px; }
  .back-button { position: absolute; left: 34px; top: 80px; }
  .favourite-button {
    position: absolute; left: 299px; top: 641px;
    width: 52px; height: 52px; border-radius: 50%;
    background: var(--accent-red);
    display: flex; align-items: center; justify-content: center;
  }
  .details { position: absolute; left: 0; top: 668px; width: 650px; text-align: center; }
  .produce-name {
    font-family: "Raleway", sans-serif; font-weight: 300;
    font-size: 52px; color: var(--title-ink);
    margin-top: 62px; line-height: 1;
  }
  .update-meta { color: var(--meta-ink); font-size: 25px; line-height: 39px; margin-top: 26px; }
  .rating {
    display: flex; align-items: center; justify-content: center; gap: 8px;
    color: var(--rating-ink); font-size: 31px; margin-top: 26px;
  }
  .divider { position: absolute; left: 0; top: 1017px; width: 650px; height: 2px; background: var(--divider); }
  .description { position: absolute; left: 0; top: 1055px; width: 650px; text-align: center; }
  .description h2 { font-weight: 400; font-size: 29px; color: var(--heading-ink); line-height: 38px; }
  .description p { font-size: 26px; color: var(--body-ink); line-height: 38px; margin-top: 12px; padding: 0 50px; }
</style>
</head>
<body>
  <main class="screen">
    <div class="hero-photo" role="img" aria-label="Photograph of red and yellow Fuji apples piled in a white porcelain tureen, one apple resting beside it"></div>

    <header class="status-bar">
      <div class="status-left">
        <div class="signal"><span class="on"></span><span class="on"></span><span class="on"></span><span></span><span></span></div>
        <span>Draftly</span>
        <svg width="20" height="16" viewBox="0 0 20 16"><path d="M2 6 A11 11 0 0 1 18 6" fill="none" stroke="#fff" stroke-width="2"/><path d="M5 9 A7 7 0 0 1 15 9" fill="none" stroke="#fff" stroke-width="2"/><circle cx="10" cy="13" r="2" fill="#fff"/></svg>
      </div>
      <span class="status-time">9:41 AM</span>
      <div class="status-right">
        <svg width="12" height="20" viewBox="0 0 12 20"><path d="M1 5 L10 14 L6 18 L6 2 L10 6 L1 15" fill="none" stroke="#fff" stroke-width="1.6"/></svg>
        <span>42%</span>
        <div class="battery"><div class="battery-level"></div></div>
      </div>
    </header>

    <svg class="back-button" width="18" height="30" viewBox="0 0 18 30" aria-label="Back"><path d="M15 2 L3 15 L15 28" fill="none" stroke="#fff" stroke-width="2"/></svg>

    <div class="favourite-button" aria-label="Favourite">
      <svg width="18" height="16" viewBox="0 0 24 22"><path d="M12 21 L2.5 11.5 A5.5 5.5 0 0 1 12 4 A5.5 5.5 0 0 1 21.5 11.5 Z" fill="#fff"/></svg>
    </div>

    <section class="details">
      <h1 class="produce-name">Fuji Apple</h1>
      <p class="update-meta">Last Updated : December 6, 2013<br>Time : 11:45 pm</p>
      <div class="rating">
        <svg width="26" height="23" viewBox="0 0 24 22"><path d="M12 21 L2.5 11.5 A5.5 5.5 0 0 1 12 4 A5.5 5.5 0 0 1 21.5 11.5 Z" fill="#4a4e55"/></svg>
        <span>9.2</span>
      </div>
    </section>

    <div class="divider"></div>

    <section class="description">
      <h2>Description and Taste</h2>
      <p>Medium to large in size the thick skin of the Fuji fruit is light red with yellow and pale speckles</p>
    </section>
  </main>
</body>
</html>
```